Kleine Werbebroschüre für Bauunternehmen (Deckblatt plus  1. und 2. Seite)
Kleine Werbebroschüre für Bauunternehmen (Deckblatt plus 1. und 2. Seite)
Zielgruppe
Private Bauherren, Familien
Aufgabenstellung
Guten Tag zusammen,
wir benötigen einen klein Broschüre für ein Bauunternehmen, welche angelehnt werden kann an das Design unserer Internetseite www.kolbe-steinbau.de. Die Broschüre soll nur aus einem Deckblatt und dann beim Aufklappen aus einer ersten und zweiten Seite bestehen, die Rückseite kann frei bleiben bzw. hier genügt ein kleiner farblicher Balken mit z. B. unseren Kontaktinformationen. Die Bilder, Logos und Texte, welche verarbeitet werden sollen, laden wir gerne über das Portal hoch. Zur ganz groben Orientierung haben wir ein Word Dokument angelegt und hochgeladen, das Hausbild auf dem Deckblatt muss nicht, aber kann eingebaut werden, es muss sich halt gut in das Gesamtbild einfügen. Wir wünschen uns eine modernes, hochwertiges und vertrauenserweckendes Design, die Website soll nur zur Orientierung gelten und Eure Kreativität nicht einschränken. Wir sind für alle Vorschläge offen. Wenn es fragen gibt, sind wir jederzeit für Euch ansprechbar.
Wir freuen uns auf Eure Vorschläge.
Jörg

```html
<!DOCTYPE html>
<html lang="de">
<head>
<meta charset="utf-8">
<title>Kolbe Steinbau – Broschüre</title>
<link href="https://fonts.googleapis.com/css2?family=Mulish:wght@400;600;700&display=swap" rel="stylesheet">
<style>
:root{
  --blue:#1d64ad;
  --blue-dark:#164f8c;
  --text:#4a4a4a;
  --muted:#666;
  --badge:#1f8a4c;
  --plan:#eef0f2;
}
*{margin:0;padding:0;box-sizing:border-box}
html,body{width:1200px;height:848px;overflow:hidden;background:#fff}
body{font-family:"Mulish",sans-serif;color:var(--text);position:relative}
.page{position:absolute;top:0;width:600px;height:848px;overflow:hidden}
.page--left{left:0}
.page--right{left:601px;width:599px}
.spine{position:absolute;left:600px;top:0;width:1.5px;height:848px;background:var(--blue)}
.abs{position:absolute}
.title{color:var(--blue);font-weight:400;font-size:30px;line-height:37.5px;letter-spacing:0}
.h2{color:var(--blue);font-weight:600;font-size:11.5px;letter-spacing:.1px}
.body{font-size:8.3px;line-height:12.75px;color:var(--text);text-align:justify;hyphens:auto}
.intro{color:var(--blue);font-size:9.2px;line-height:14.25px;hyphens:auto}
.lead{font-size:8.2px;line-height:14.25px;color:var(--muted);hyphens:auto}
.full{font-size:8.6px;line-height:13.4px;text-align:justify}
.photo-family{left:330px;top:104px;width:250px;height:176px;border-radius:30px;
  background:radial-gradient(ellipse at 50% 45%,#ecd2b6 0%,#f4e7da 50%,#fbf7f3 80%,#fff 100%)}
.badge{width:44px;height:58px;background:var(--badge);border-radius:4px 4px 22px 22px}
.blist{list-style:none}
.blist li{position:relative;padding-left:14px;margin-bottom:10px}
.blist li::before{content:"";position:absolute;left:3px;top:4px;width:4px;height:4px;border-radius:50%;background:var(--blue)}
.footer-url{font-size:9px;color:var(--blue-dark);letter-spacing:.3px}
.page-icon{width:18px;height:16px}
.subtitle{font-size:10px;line-height:16.5px;text-align:center;color:var(--text)}
.subtitle span{color:var(--blue)}
.house{left:89px;width:193px;background:linear-gradient(180deg,#bcd6ee 0%,#e6eef4 45%,#8fae6e 80%,#6f8f52 100%)}
.plan{background:var(--plan);border:1px solid #d5d9dd}
.tag{left:38px;height:22px;padding:0 12px 0 10px;background:var(--blue-dark);color:#fff;font-size:10px;font-weight:600;
  line-height:22px;letter-spacing:.5px;clip-path:polygon(0 0,88% 0,100% 50%,88% 100%,0 100%)}
.spec{font-size:8.8px;line-height:12.75px;color:var(--text);hyphens:auto;overflow-wrap:break-word}
.spec::before{content:"";position:absolute;left:-13px;top:3px;width:0;height:0;border-left:6px solid var(--blue-dark);border-top:3.5px solid transparent;border-bottom:3.5px solid transparent}
.brand{left:281px;top:820px;height:24px;display:flex;align-items:center;gap:4px;background:var(--blue-dark);padding:0 6px;color:#fff;font-size:10px;font-weight:600;letter-spacing:2px}
.brand i{display:block;width:10px;height:10px;background:#fff}
</style>
</head>
<body>
<div class="spine"></div>

<section class="page page--left">
  <div class="abs photo-family" role="img" aria-label="Foto einer lächelnden Familie mit zwei Kindern"></div>
  <h1 class="abs title" style="left:41px;top:32px">SIE SUCHEN EIN TRAUMHAUS<br>FÜR IHRE FAMILIE?</h1>
  <div class="abs badge" style="left:518px;top:39px" aria-label="Prüfsiegel"></div>

  <p class="abs intro" style="left:41px;top:118px;width:275px">Kolbe Steinbau ist spezialisiert auf den Bau von Massivhäusern - deutschlandweit. Wir bauen für Sie solide Stein auf Stein und auf Wunsch nach den Standards für ein förderfähiges FBW-Effizienzhaus (Förderbank für Wohnbau). Zur Freude der Umwelt und Ihrer Brieftasche.</p>
  <p class="abs lead" style="left:41px;top:197px;width:255px">Zur unabhängigen und objektiven Bauüberwachung arbeiten wir mit der PRÜFRING-Bauüberwachung zusammen. Die Zertifizierung durch den PRÜFRING garantiert höchste Immobilienqualität und Sicherheit und ist in jedem unserer Angebote bereits standardmäßig inklusive - zu Ihrer Sicherheit.</p>
  <p class="abs full" style="left:41px;top:279px;width:519px">Von der Erstberatung bis hin zur schlüsselfertigen Übergabe Ihres Massivhauses bieten wir als Totalübernehmer ein komplettes Leistungsportfolio für unsere Kunden. Mit unseren Fachberatern, Bauingenieuren, Architekten sowie unseren angeschlossenen Handwerks-Meisterbetrieben gewährleisten wir unseren Kunden PRÜFRING zertifizierte Massivhaus-Qualität.</p>

  <h2 class="abs h2" style="left:40px;top:342px">WARUM MASSIV BAUEN</h2>
  <p class="abs body" style="left:40px;top:361px;width:170px">In erster Linie heißt massiv Bauen, wertbeständig und nachhaltig zu bauen.<br>Mittel- und langfristig gesehen hat ein Massivhaus einen wesentlich höheren Wiederverkaufswert als ein Fertighaus. Die Nutzungsdauer eines Hauses in Massivbauweise wird mit ca. 100 Jahren beziffert. Dies wird beim Massivhausbau durch immer günstigere Konditionen der Banken und Versicherungen honoriert. Eine individuelle Planung ist bei Massivhäusern problemlos möglich.</p>

  <h2 class="abs h2" style="left:40px;top:531px">BAUZEIT</h2>
  <p class="abs body" style="left:40px;top:550px;width:170px">Von Fertighausanbietern wird meist mit einer sehr kurzen Errichtungszeit des Rohbaus geworben, was aber nur einen relativ kleinen Zeitabschnitt der Gesamtbauzeit betrifft.<br>Eine kurze Montagezeit verschleiert oft die lange Vorlaufzeit der Fertighaushersteller für die Produktion bis zur Montage. Deswegen spielt ein Zeitvorteil gegenüber der Massivbauweise keine Rolle.</p>

  <h2 class="abs h2" style="left:40px;top:694px">RAUMKLIMA</h2>
  <p class="abs body" style="left:40px;top:713px;width:170px">Ein Massivhaus verfügt über eine sehr gute Wärmespeicherfähigkeit. Dadurch, dass das Mauerwerk Wärme, sowohl von außen als auch von innen absorbiert, herrschen zu jeder Jahreszeit angenehme Temperaturen im Inneren. Außerdem sind massive Wände in der Lage die Feuchtigkeit zu regulieren, was ein gesundes Raumklima im ganzen Haus garantiert.</p>

  <h2 class="abs h2" style="left:241px;top:342px">SCHALL - UND BRANDSCHUTZVERHALTEN</h2>
  <p class="abs body" style="left:241px;top:361px;width:319px;line-height:13.5px">Aufgrund der höheren Dichte der Baustoffe, schützt ein Massivhaus seine Bewohner wesentlich besser vor äußerer, ständig zunehmender Lärmeinwirkung aus der Umwelt.<br>Durch die mineralischen, nicht brennbaren Baustoffe wird eine Brandverbreitung wesentlich vermindert. Zudem entstehen keine giftigen Rauchgase.<br>Wasserschäden, wie sie durch jede Waschmaschine oder durch Löschen eines Brandes entstehen können, haben im Massivhaus aufgrund der diffusionsoffenen Eigenschaften der Bauteile nur kleine Auswirkungen und trocknen leicht wieder aus, ohne bleibende Schäden zu hinterlassen.</p>

  <h2 class="abs h2" style="left:241px;top:499px">WÄRMESCHUTZVERHALTEN</h2>
  <p class="abs body" style="left:241px;top:518px;width:319px;line-height:13.5px">Die heutigen Baustoffe, die bei der Herstellung des massiven Außenmauerwerks verwendet werden, kommen denen der Holzrahmenbauweise in vielen Punkten zuvor:</p>
  <ul class="abs blist body" style="left:241px;top:563px;width:319px">
    <li style="margin-bottom:13px">In einem Haus in Holzrahmenbauweise lebt man quasi in einer Plastiktüte um der Energieeinsparverordnung zu genügen. Das Außenmauerwerk eines Massivhauses hingegen ist diffusionsoffen, dadurch wird die Feuchtigkeit die als Dampf oder Kondensat durch Waschen, Kochen oder Duschen anfällt ausgeglichen. Es entsteht ein deutlich merkbares gesünderes Raumklima ohne Gefahr der Schimmelbildung.</li>
    <li style="margin-bottom:13px">In den massiven Innenwänden wird Wärme im Winter gespeichert. So muss nach einem Lüftungsvorgang nicht die ganze Raumluft neu aufgeheizt werden. Im Sommer wird unnötige Wärme gespeichert und es bleibt im Raum kühler.</li>
    <li>Anbieter von Fertighäusern versuchen meist mit dem guten Wärmedämmverhalten ihrer Außenwandkonstruktion zu punkten. Außenwände sind aber nur an ca. 15% des gesamten Energieverlustes eines Wohnhauses beteiligt.<br>Baukosten<br>Studien zum Kostenvergleich sowie der tägliche Wettbewerb in den Bereichen Fertighaus versus Massivhaus belegen, dass massive Bauweise bei gleichem Ausstattungsstandard nicht teurer als Holzrahmenbauweise (Fertighaus) ist.</li>
  </ul>

  <div class="abs footer-url" style="left:412px;top:827px">www.kolbe-steinbau.de</div>
  <svg class="abs page-icon" style="left:542px;top:820px" viewBox="0 0 18 16"><path d="M2 7 9 1l7 6M4 6v9h10V6" fill="none" stroke="#1d64ad" stroke-width="1.4"/><text x="9" y="13.5" font-size="7" text-anchor="middle" fill="#1d64ad" font-family="Mulish,sans-serif">2</text></svg>
</section>

<section class="page page--right">
  <h1 class="abs title" style="left:0;width:599px;text-align:center;top:30px;font-size:33px">TYPENHÄUSER</h1>
  <p class="abs subtitle" style="left:0;width:599px;top:72px">Auf unserer Internetseite <span>www.kolbe-steinbau.de</span> finden Sie eine große Auswahl beliebten Typenhäusern.<br>Natürlich sind alle unsere Typenhäuser flexibel planbar bezüglich der Grundrisse und Raumaufteilung.</p>

  <div class="abs house" style="top:118px;height:83px" role="img" aria-label="Foto Einfamilienhaus SOLARIS"></div>
  <div class="abs tag" style="top:179px">SOLARIS</div>
  <div class="abs plan" style="left:92px;top:212px;width:90px;height:80px" role="img" aria-label="Grundriss Erdgeschoss"></div>
  <div class="abs plan" style="left:200px;top:212px;width:80px;height:80px" role="img" aria-label="Grundriss Dachgeschoss"></div>

  <div class="abs house" style="top:295px;height:82px" role="img" aria-label="Foto Einfamilienhaus AMARO"></div>
  <div class="abs tag" style="top:356px">AMARO</div>
  <div class="abs plan" style="left:93px;top:387px;width:88px;height:80px" role="img" aria-label="Grundriss Erdgeschoss"></div>
  <div class="abs plan" style="left:190px;top:384px;width:90px;height:83px" role="img" aria-label="Grundriss Dachgeschoss"></div>

  <div class="abs house" style="top:471px;height:83px" role="img" aria-label="Foto Einfamilienhaus SERENA"></div>
  <div class="abs tag" style="top:532px">SERENA</div>
  <div class="abs plan" style="left:97px;top:560px;width:80px;height:80px" role="img" aria-label="Grundriss Erdgeschoss"></div>
  <div class="abs plan" style="left:194px;top:556px;width:80px;height:86px" role="img" aria-label="Grundriss Dachgeschoss"></div>

  <div class="abs house" style="top:652px;height:83px" role="img" aria-label="Foto Stadtvilla GRANDIS"></div>
  <div class="abs tag" style="top:713px">GRANDIS</div>
  <div class="abs plan" style="left:99px;top:740px;width:76px;height:82px" role="img" aria-label="Grundriss Erdgeschoss"></div>
  <div class="abs plan" style="left:194px;top:740px;width:76px;height:82px" role="img" aria-label="Grundriss Obergeschoss"></div>

  <h2 class="abs h2" style="left:326px;top:116px;font-size:12px">BAU - UND LEISTUNGSBESCHREIBUNG</h2>
  <p class="abs body" style="left:326px;top:134px;width:232px;font-size:8.4px;line-height:15.75px;text-align:left">Mit der übersichtlichen Bau- und Leistungsbeschreibung, einer transparenten Kalkulation sowie einer Festpreis- und Bauzeitgarantie mit Zahlungsplan nach Baufortschritt, haben Sie immer alles genau im Blick. Die Zufriedenheit unserer Kunden steht bei uns an erster Stelle. Hier ein kurzer Überblick über die groben Eckpunkte unserer Bau- und Leistungsbeschreibung:</p>

  <div class="abs spec" style="left:328px;top:254px;width:104px">Rohbauhöhe EG 275 cm, in allen anderen Wohngeschossen 262,5 cm</div>
  <div class="abs spec" style="left:328px;top:318px;width:104px">Massive Außenwände aus hochdämmenden Tonwerk Lindau Porit Hochlochziegeln Typ „Typ L10“</div>
  <div class="abs spec" style="left:328px;top:395px;width:104px">Alle Innenwände ebenfalls massiv</div>
  <div class="abs spec" style="left:328px;top:433px;width:104px">Dacheindeckung mit Betondachsteinen der Marke DACHFELS</div>
  <div class="abs spec" style="left:328px;top:483px;width:104px">Die Regenrinnen und Regenfallrohre aus Titanzinkblech</div>
  <div class="abs spec" style="left:326px;top:537px;width:108px">Alle Wohnräume erhalten einen Zementestrich mit Fußbodenheizung</div>
  <div class="abs spec" style="left:326px;top:588px;width:108px">Fliesenbeläge im Wert von 25,00 € / m²</div>
  <div class="abs spec" style="left:326px;top:627px;width:108px">Sanitärobjekte von „Keramhaus &amp; Sohn“ sowie Dusch- und Badewanne von „Wannwerk“ mit Armaturen von „Aquaro“</div>
  <div class="abs spec" style="left:326px;top:703px;width:104px">Innentüren als Röhrenspansteg-Türblättern, hochwertig laminiert.</div>
  <div class="abs spec" style="left:326px;top:767px;width:104px">Zweiholm-Stahltreppe mit Trittstufen aus Buche (stabverleimt)</div>

  <div class="abs spec" style="left:453px;top:254px;width:106px">Kunststofffenster mit 5-Kammer-Profil, Wärmeschutz&shy;verglasung, Rollladen und Natursteinfenster&shy;bänken</div>
  <div class="abs spec" style="left:453px;top:330px;width:100px">Außenputz als zweila&shy;giger mineralischer Strukturputz + Egalisa&shy;tionsanstrich</div>
  <div class="abs spec" style="left:453px;top:395px;width:100px">Gasbrennwertheizung&shy;sanlage mit Solaranlage von „Thermora“</div>
  <div class="abs spec" style="left:453px;top:445px;width:100px">Innenputz als einlagiger Gipsputz</div>
  <div class="abs spec" style="left:453px;top:483px;width:100px">Dach gedämmt mit 20 cm Mineralwolle der Marke „Isolan“</div>
  <div class="abs spec" style="left:455px;top:537px;width:100px">Bodenbeläge aus Laminat im Wert von 15,00 € / m²</div>
  <div class="abs spec" style="left:455px;top:589px;width:104px">Wände tapeziert mit „Mühltaler“ Rauhfaser sämtliche Planungs- und Bauleitungsleistungen</div>
  <div class="abs spec" style="left:455px;top:653px;width:104px">PRÜFRING-Bauüberwachung mit Zertifikat Festpreis-Garantie Eigenleistungen möglich</div>

  <div class="abs badge" style="left:468px;top:724px;width:64px;height:84px;border-radius:4px 4px 32px 32px" aria-label="Prüfsiegel"></div>

  <div class="abs brand">kolbe<i></i></div>
  <div class="abs footer-url" style="left:419px;top:824px">www.kolbe-steinbau.de</div>
  <svg class="abs page-icon" style="left:548px;top:818px" viewBox="0 0 18 16"><path d="M2 7 9 1l7 6M4 6v9h10V6" fill="none" stroke="#1d64ad" stroke-width="1.4"/><text x="9" y="13.5" font-size="7" text-anchor="middle" fill="#1d64ad" font-family="Mulish,sans-serif">3</text></svg>
</section>
</body>
</html>
```